Fun Language School in San Diego, CA - We want cool Business Card

We need a new business card design for our new logo. We are a language school in beautiful San Diego, California. Our target is students from all over the world who age from 18 to 25. They come to our school to learn English. Our school has a modern look, trending and fun place. We are the only language school who use tablets in class. We are student oriented, Students Come First is our slogan. We are re-branding ourselves with a new logo. We would like to see a designs that use our new logo and it should reflect the feel of young, fun, modern, high-tech and attractive to young people.
I've seen some business card designs with transparent look, unusual shapes, we are open to any cool ideas. Thank you very much!

In order for you to know more about our school, here are the links to our Youtube Channel and Facebook.

Youtube: https://www.vidloop.example/channel/ZXpo84kR-21bvn5wQ7t2LmHd
Facebook: https://www.friendspace.example/TVSchool

Target Market(s)

Our target is students from all over the world who age from 18 to 25. International students.

Industry/Entity Type

School

Font styles to use
Sans Serif

Requirements
Must have
• Our new logo. Name, title and address.
Should not have
• Other colors other than the ones we have in our logo. Characters are fine.

```html
<!DOCTYPE html>
<html lang="en">
<head>
<meta charset="utf-8">
<title>Tidewave School – Business Card</title>
<link rel="stylesheet" href="https://fonts.googleapis.com/css2?family=Open+Sans:wght@400;600;700&display=swap">
<style>
  :root {
    --page-bg: #d9d6d1;
    --card-bg: #f5f4f1;
    --ink-dark: #3b3b3b;
    --ink-body: #404244;
    --brand-grey: #5c666a;
    --teal: #4ba8a6;
    --olive: #aab555;
    --ocean: #2f7b9b;
    --icon-green: #86a83c;
    --title-blue: #2e7590;
  }
  * { box-sizing: border-box; margin: 0; padding: 0; }
  html, body {
    width: 1200px; height: 970px; overflow: hidden;
    background: var(--page-bg);
    font-family: "Open Sans", sans-serif;
  }
  .card {
    position: absolute; left: 60px; top: 185px;
    width: 1080px; height: 600px;
    background: var(--card-bg);
    box-shadow: 0 10px 30px rgba(0,0,0,0.12);
    overflow: hidden;
  }
  .brand {
    position: absolute; left: 48px; top: 270px;
    display: flex; align-items: center; gap: 18px;
  }
  .brand-dot {
    width: 70px; height: 70px; border-radius: 50%;
    background: var(--teal);
  }
  .brand-name {
    font-size: 40px; font-weight: 400; color: var(--brand-grey);
    letter-spacing: 0.5px;
  }
  .holder {
    position: absolute; left: 534px; top: 132px;
  }
  .holder-name {
    font-size: 37px; font-weight: 700; color: var(--ink-dark);
    letter-spacing: 1.5px; line-height: 48px;
  }
  .holder-title {
    margin-top: 8px;
    font-size: 30px; font-weight: 400; color: var(--title-blue);
    letter-spacing: 1px; line-height: 40px;
  }
  .address {
    position: absolute; left: 534px; top: 262px;
    font-size: 23px; color: var(--ink-body); letter-spacing: 0.6px;
  }
  .contacts {
    position: absolute; left: 538px; top: 318px;
    list-style: none;
  }
  .contact {
    display: flex; align-items: center; height: 42px;
    font-size: 23px; color: var(--ink-body); letter-spacing: 0.8px;
  }
  .contact svg { width: 22px; height: 22px; margin-right: 26px; flex: none; }
  .color-band {
    position: absolute; left: 0; bottom: 0; width: 100%; height: 36px;
    display: flex;
  }
  .band-teal { width: 345px; background: var(--teal); }
  .band-olive { width: 370px; background: var(--olive); }
  .band-ocean { flex: 1; background: var(--ocean); }
</style>
</head>
<body>
  <main class="card">
    <div class="brand">
      <span class="brand-dot" aria-hidden="true"></span>
      <span class="brand-name">Tidewave School</span>
    </div>

    <div class="holder">
      <p class="holder-name">Marla Quent</p>
      <p class="holder-title">President</p>
    </div>

    <p class="address">Pelican Row, Coral Bay, CB 00410, Maredonia</p>

    <ul class="contacts">
      <li class="contact">
        <svg viewBox="0 0 22 22" aria-hidden="true"><rect x="6" y="2" width="10" height="18" rx="2" fill="none" stroke="var(--icon-green)" stroke-width="2"/><circle cx="11" cy="16.5" r="1.2" fill="var(--icon-green)"/></svg>
        +00 555 010 482
      </li>
      <li class="contact">
        <svg viewBox="0 0 22 22" aria-hidden="true"><path d="M3 8 Q11 2 19 8 L17 10 L14 8.5 L14 7 Q11 6 8 7 L8 8.5 L5 10 Z" fill="var(--icon-green)"/><rect x="5" y="12" width="12" height="7" rx="1.5" fill="var(--icon-green)"/><circle cx="11" cy="15.5" r="1.8" fill="var(--card-bg)"/></svg>
        +00 55 5 010 777
      </li>
      <li class="contact">
        <svg viewBox="0 0 22 22" aria-hidden="true"><rect x="2" y="5" width="18" height="12" fill="none" stroke="var(--icon-green)" stroke-width="2"/><path d="M2 5 L11 12 L20 5" fill="none" stroke="var(--icon-green)" stroke-width="2"/></svg>
        sales@tidewaveschool.example
      </li>
      <li class="contact">
        <svg viewBox="0 0 22 22" aria-hidden="true"><circle cx="11" cy="11" r="8.5" fill="none" stroke="var(--icon-green)" stroke-width="2"/><ellipse cx="11" cy="11" rx="3.5" ry="8.5" fill="none" stroke="var(--icon-green)" stroke-width="1.6"/><path d="M2.5 11 H19.5" stroke="var(--icon-green)" stroke-width="1.6"/></svg>
        www.tidewaveschool.example
      </li>
    </ul>

    <div class="color-band" aria-hidden="true">
      <span class="band-teal"></span>
      <span class="band-olive"></span>
      <span class="band-ocean"></span>
    </div>
  </main>
</body>
</html>
```